Plakate für ein Malereibetreib
Zielgruppe
Wir sind ein familiär geführter Malereibetreib (7 Mitarbeiter) mit Aufträgen in den Gewerken Fassadenrenovierungen und Balkonabdichtung.
Wir sind auf der Suche nach kräftigen, arbeitswilligen Mitarbeiter, die Freude daran haben, mit Ihren Händen, mehrheitlich draussen zu arbeiten und dafür gut bezahlt werden.
Aufgabenstellung
Das Plakat wird auf eine Fassade mit direktem Blick von einem großen Supermarktparkplatz montiert.
Die Größe wird ca. 4m x 4 m betragen.
Wir möchten unser Plakat NICHT im Stil unserer Homepage gestaltet haben. Die ist uns für den Zweck der Mitarbeitersuche zu brav.
Ebenso bitte KEINE 'klassischen' Stock-Bilder (Malerpinsel, bunte Farbdosen, angeschmierte Leitern) verwendet werden.
Das Plakat soll eher ohne Fotos, sondern lieber mit Grafiken (Comic, Zeichnungen...) gestaltet sein.
Es soll zum witzigen, spontanen, sehr auffallenden, kurzzeitigen Aufruf nach Fachkräften für unseren Betrieb dienen.
Uns gefallen Retro-Schriften sehr gut.
Als Kontaktdaten soll auf dem Plakat nur unser Firmenname 'brolting', Telefonnummer 089 52 17 63 und Website www.brolting-gmbh.de stehen.

```html
<!DOCTYPE html>
<html lang="de">
<head>
<meta charset="utf-8">
<title>brolting – Wir suchen Fachkräfte</title>
<link rel="stylesheet" href="https://fonts.googleapis.com/css2?family=Londrina+Solid:wght@400;900&family=Josefin+Sans:wght@300&family=Open+Sans:wght@400;600&display=swap">
<style>
  :root {
    --green: #0d7459;
    --teal: #62b3a3;
    --yellow: #f5b719;
    --orange: #e2761c;
    --white: #ffffff;
    --grey: #7a7a7a;
  }
  * { margin: 0; padding: 0; box-sizing: border-box; }
  html, body { width: 1200px; height: 800px; overflow: hidden; background: var(--white); }
  .poster {
    position: relative;
    width: 1200px;
    height: 800px;
    background: var(--green);
    overflow: hidden;
  }
  .brush-bands { position: absolute; inset: 0; width: 1200px; height: 690px; }
  .quote {
    position: absolute;
    top: 150px;
    left: 0;
    width: 1200px;
    font-family: "Londrina Solid", "Impact", sans-serif;
    font-weight: 900;
    font-size: 104px;
    line-height: 0.98;
    letter-spacing: 3px;
    color: var(--yellow);
    text-transform: uppercase;
  }
  .quote-line { display: block; white-space: nowrap; }
  .quote-line--first { padding-left: 250px; }
  .quote-line--second { padding-left: 150px; }
  .quote-line--third { padding-left: 215px; }
  .quote-accent { color: var(--orange); }
  .quote-author {
    position: absolute;
    top: 478px;
    left: 495px;
    font-family: "Londrina Solid", "Impact", sans-serif;
    font-weight: 400;
    font-size: 38px;
    letter-spacing: 2px;
    color: var(--orange);
    text-transform: uppercase;
  }
  .website {
    position: absolute;
    top: 565px;
    left: 0;
    width: 1200px;
    text-align: center;
    font-family: "Josefin Sans", "Helvetica", sans-serif;
    font-weight: 300;
    font-size: 52px;
    color: var(--yellow);
  }
  .footer {
    position: absolute;
    left: 0;
    bottom: 0;
    width: 1200px;
    height: 110px;
    background: var(--white);
    font-family: "Open Sans", "Arial", sans-serif;
  }
  .footer-call {
    position: absolute;
    top: 34px;
    left: 45px;
    font-size: 30px;
    font-weight: 600;
    color: var(--orange);
  }
  .footer-phone {
    position: absolute;
    top: 34px;
    left: 500px;
    font-size: 30px;
    font-weight: 600;
    color: var(--orange);
  }
  .brand {
    position: absolute;
    right: 30px;
    bottom: 22px;
    font-family: "Open Sans", "Arial", sans-serif;
    white-space: nowrap;
  }
  .brand-name { font-size: 24px; font-weight: 400; color: var(--orange); letter-spacing: 1px; }
  .brand-trade { font-size: 14px; font-weight: 400; color: var(--grey); margin-left: 4px; }
</style>
</head>
<body>
  <main class="poster">
    <svg class="brush-bands" viewBox="0 0 1200 690" aria-hidden="true">
      <polygon points="0,140 420,0 620,0 0,330" fill="var(--teal)"/>
      <polygon points="0,210 240,80 190,140 0,255" fill="var(--teal)" opacity="0.6"/>
      <polygon points="1200,300 1200,690 880,690" fill="var(--teal)"/>
      <polygon points="1200,520 1200,690 1080,690" fill="var(--green)" opacity="0.5"/>
    </svg>

    <h1 class="quote">
      <span class="quote-line quote-line--first">„Jeder Tag an</span>
      <span class="quote-line quote-line--second">dem man <span class="quote-accent">malt</span> ist</span>
      <span class="quote-line quote-line--third">ein guter Tag.“</span>
    </h1>
    <p class="quote-author">-Hanno Pinsler</p>

    <p class="website">www.brolting-gmbh.de</p>

    <footer class="footer">
      <p class="footer-call">Wir suchen Fachkräfte!</p>
      <p class="footer-phone">Tel.: +49 089 52 17 63</p>
      <p class="brand"><span class="brand-name">brolting</span><span class="brand-trade">malerarbeiten</span></p>
    </footer>
  </main>
</body>
</html>
```